Larkfield Financial Plans

I am looking for a complete resdesign of my small financial presentation. This is a Word Doc/PDF that I print off when meeting with people in private. I often present my "two pager" that I have been using for years and years. It tells them the basics of what I do, how I help people and foundational financial principles.

I have recently gone out on my own in business and have completely rebranded. This presentation is my most used tool, so it is the first of many things I would like to redo. I am hoping it will somehow coordinate with the colors of my business, not necessarily the EXACT same 3 colors everywhere, but have the design colors compliment.

I've uploaded all my logo designs, as well as the current "two-pager". I am not against it going to 3 pages if needed. As it will still land on 2 pages with duplex printing.

It has always been VERY simple. I am wanting it built into a more professional and design specific format, to show off my branding, without being over cluttered.

I am completely open to ANY graphics changes. Obviously some are very novice, the house on the last page has always been overly simplified.

```html
<!DOCTYPE html>
<html lang="en">
<head>
<meta charset="utf-8">
<title>Larkfield Financial Plans – Two Pager</title>
<link href="https://fonts.googleapis.com/css2?family=Jost:wght@500;600;700&family=Roboto:wght@400;500;700&display=swap" rel="stylesheet">
<style>
:root{
  --navy:#111e33;
  --green:#0aaf45;
  --grey:#868c95;
  --light:#eef2f8;
  --panel:#f2f4f6;
  --stage:#9c9c9c;
  --ink:#1b2433;
}
*{box-sizing:border-box;margin:0;padding:0}
html,body{width:1200px;height:774px;overflow:hidden}
body{background:var(--stage);font-family:'Roboto',sans-serif;color:var(--ink);position:relative}
.page{position:absolute;top:55px;width:514px;height:664px;background:#fff;box-shadow:0 3px 10px rgba(0,0,0,.25);overflow:hidden}
.page-one{left:62px}
.page-two{left:624px}
.abs{position:absolute}

/* header */
.header{position:absolute;left:0;top:0;width:514px;height:59px}
.header svg{position:absolute;left:0;top:0}
.header-title{position:absolute;left:45px;top:17px;font-family:'Jost',sans-serif;font-weight:500;font-size:16.5px;color:#fff;letter-spacing:.2px}
.brand{position:absolute;left:356px;top:15px;width:112px;text-align:center;font-family:'Jost',sans-serif;font-weight:600;color:var(--navy);line-height:1}
.brand-name{font-size:17px;letter-spacing:.3px}
.brand-tag{font-size:6px;letter-spacing:1.4px;margin-top:3px}

/* challenge cards */
.challenge-card{position:absolute;top:79px;width:119px;height:171px;border:1px solid #c9ced6;border-radius:17px;padding:0 8px}
.card-icon{position:absolute;left:8px;top:10px;width:31px;height:31px;border-radius:50%;background:var(--green)}
.card-title{position:absolute;left:8px;top:47px;font-size:7.6px;font-weight:700;color:var(--navy)}
.card-body{position:absolute;left:8px;right:6px;top:61px;font-size:4.4px;line-height:7.4px;color:#3a4250;text-transform:uppercase}
.card-body p{padding-left:8px;position:relative}
.card-body p.point::before{content:"";position:absolute;left:0;top:2px;width:4px;height:4px;border:1px solid var(--green);border-radius:50%}
.card-body p.source{font-weight:500;color:var(--ink);margin:3px 0 6px}

/* who section */
.who{position:absolute;left:0;top:270px;width:514px;height:191px;background:var(--light)}
.section-heading{position:absolute;left:0;width:514px;text-align:center;font-family:'Jost',sans-serif;font-weight:600;color:var(--navy);font-size:17px;letter-spacing:.3px}
.underline{position:absolute;height:2px;background:var(--green)}
.service{position:absolute;top:75px;width:63px;height:49px;background:#fff;border-radius:7px;border:1px solid var(--green);font-size:6.2px;font-weight:700;color:var(--navy);text-align:center;display:flex;align-items:center;justify-content:center;padding-top:8px;line-height:8.5px}
.service.dark{border-color:var(--navy)}
.service-icon{position:absolute;left:19px;top:-13px;width:25px;height:25px;border-radius:50%;background:var(--green);border:2px solid #fff}
.service.dark .service-icon{background:var(--navy)}
.pill{position:absolute;left:200px;top:140px;width:114px;height:21px;border-radius:11px;background:var(--navy);color:var(--green);font-size:6.6px;font-weight:700;display:flex;align-items:center;justify-content:center}

/* how section */
.flow-label{position:absolute;font-size:5px;font-weight:700;color:var(--navy)}
.goal-list{position:absolute;left:211px;top:526px;list-style:none}
.goal-list li{display:flex;align-items:center;gap:8px;height:24.3px;font-size:8.8px;font-weight:700;color:var(--navy)}
.tick{width:8px;height:8px;border-radius:50%;background:var(--green);display:inline-block;position:relative;flex:none}
.tick::after{content:"";position:absolute;left:2.5px;top:1.2px;width:2px;height:3.8px;border:solid #fff;border-width:0 1.2px 1.2px 0;transform:rotate(45deg)}
.partner{position:absolute;width:47px;height:16px;border-radius:5px;background:#dcdfe3}

/* footer */
.footer{position:absolute;left:0;top:640px;width:514px;height:17px;background:var(--green);color:#fff;font-size:5.6px;display:flex;align-items:center;padding-left:45px;gap:8px}
.footer span{display:flex;align-items:center;gap:3px}
.page-num{position:absolute;left:451px;top:640px;width:17px;height:17px;border-radius:50%;background:#fff;border:1.5px solid var(--green);font-size:5.6px;font-weight:700;color:var(--navy);display:flex;align-items:center;justify-content:center}

/* rule of 72 table */
.rule-table{position:absolute;left:46px;top:94px;border-collapse:collapse;table-layout:fixed;width:422px}
.rule-table th{height:27px;font-size:6.8px;font-weight:700;color:#fff;background:var(--green);border-right:1px solid #fff}
.rule-table th.age{background:var(--navy);text-align:left;padding-left:10px}
.rule-table td{height:23.3px;font-size:6px;text-align:center;border:1px solid #d7dbe0;color:var(--ink)}
.rule-table td.age{text-align:left;padding-left:10px;font-weight:700}
.double-note{position:absolute;top:343px;width:68px;text-align:center;font-size:5.6px;font-weight:700;line-height:9px;color:var(--navy)}

/* tax cards */
.tax-card{position:absolute;top:428px;width:97px;height:130px;border-radius:20px;color:#fff;padding:0 10px}
.tax-card.navy{background:var(--navy)}
.tax-card.green{background:var(--green)}
.tax-card.grey{background:var(--grey)}
.tax-icon{position:absolute;left:10px;top:15px;width:31px;height:31px;border-radius:50%;background:#fff}
.tax-title{position:absolute;left:10px;top:52px;font-size:8px;font-weight:700}
.tax-points{position:absolute;left:10px;right:6px;top:67px;font-size:4.4px;line-height:7.4px;font-weight:500;text-transform:uppercase}
.tax-points p{position:relative;padding-left:8px;margin-bottom:3.5px}
.tax-points p::before{content:"";position:absolute;left:0;top:1.8px;width:4px;height:4px;border:1px solid #fff;border-radius:50%}
.tax-foot{position:absolute;left:10px;top:112px;font-size:5px;font-weight:700;letter-spacing:1.2px;color:#9fe3b7}
.tax-card.green .tax-foot{color:#fff}
.tax-card.grey .tax-foot{color:#fff}
.cover-line{position:absolute;left:0;top:577px;width:514px;text-align:center;font-size:8px;font-weight:700;color:var(--navy);word-spacing:1px}
.cover-line i{font-style:normal;margin:0 9px}
</style>
</head>
<body>

<!-- PAGE ONE -->
<section class="page page-one">
  <div class="header">
    <svg width="514" height="59" viewBox="0 0 514 59">
      <rect width="514" height="59" fill="#f2f4f6"/>
      <polygon points="0,0 285,0 320,33 292,59 0,59" fill="#111e33"/>
      <polygon points="304,0 322,0 358,59 340,59" fill="#868c95"/>
      <polygon points="292,59 316,35 341,59" fill="#0aaf45"/>
    </svg>
    <h1 class="header-title">THE FINANCIAL CHALLENGE</h1>
    <div class="brand"><div class="brand-name">LARKFIELD</div><div class="brand-tag">FINANCIAL PLANS</div></div>
  </div>

  <article class="challenge-card" style="left:68px">
    <div class="card-icon"><svg width="31" height="31" viewBox="0 0 31 31"><text x="15.5" y="20" text-anchor="middle" font-family="Roboto,sans-serif" font-size="13" font-weight="700" fill="#fff">$</text></svg></div>
    <h2 class="card-title">SAVINGS</h2>
    <div class="card-body">
      <p class="point">49% of Canadian employees are living paycheque to paycheque. 25% of Canadians are unable to cover an unexpected $500 expense</p>
      <p class="source">-National Stats Bureau (Feb 2023)</p>
      <p class="point">25% of Canadians need to access their retirement savings early. 20% of Canadians have no savings. 39% of Canadians aged 55-65 have less than $5,000 in savings.</p>
      <p class="source">-Federal Savings Office (June 2023)</p>
    </div>
  </article>

  <article class="challenge-card" style="left:198px">
    <div class="card-icon"><svg width="31" height="31" viewBox="0 0 31 31"><path d="M8 20h15v3H8z M12 18v-6h7v6" fill="#fff"/><text x="15.5" y="17" text-anchor="middle" font-family="Roboto,sans-serif" font-size="7" font-weight="700" fill="#0aaf45">$</text></svg></div>
    <h2 class="card-title">DEBT</h2>
    <div class="card-body">
      <p class="point">The average Canadian has $22,131 in consumer debt. Which excludes</p>
      <p class="source">mortgages.-CreditView (Aug 2024)</p>
      <p class="point">Over 55% of Canadians hold credit card debt and the total Canadian household debt has increased to $2.52trillion, including consumer credit, mortgage and non-mortgage loans.</p>
      <p class="source">-Northern Bankers Group (Aug 2024)</p>
    </div>
  </article>

  <article class="challenge-card" style="left:327px">
    <div class="card-icon"><svg width="31" height="31" viewBox="0 0 31 31"><rect x="9" y="8" width="10" height="14" rx="1.5" fill="#fff"/><path d="M17 16l4-1.5 4 1.5v3c0 2.5-2 4-4 4.5-2-.5-4-2-4-4.5z" fill="#fff" stroke="#0aaf45" stroke-width="1"/></svg></div>
    <h2 class="card-title">INSURANCE</h2>
    <div class="card-body">
      <p class="point">45% of Canadians do not have individual life insurance coverage, but 48% say their families would face financial trouble within 6 months of losing someone.</p>
      <p class="source">-Lifemark Research (Apr 2023)</p>
      <p class="point">2-in-5 Canadians (43% women / 44% men) will be diagosed with a form of cancer or other critical illness during their lifetime. Every 7 seconds.</p>
      <p class="source">-Health Data Hub (June 2024)</p>
    </div>
  </article>

  <section class="who">
    <h2 class="section-heading" style="top:24px">WHO ARE WE AND WHAT DO WE DO?</h2>
    <div class="underline" style="left:239px;top:48px;width:36px"></div>

    <div class="service" style="left:45px"><span class="service-icon"><svg width="21" height="21" viewBox="0 0 21 21"><circle cx="10.5" cy="10.5" r="6" fill="none" stroke="#fff" stroke-width="1.3"/><text x="10.5" y="13.5" text-anchor="middle" font-size="8" font-weight="700" fill="#fff" font-family="Roboto,sans-serif">$</text></svg></span>CASH FLOW</div>
    <div class="service dark" style="left:117px"><span class="service-icon"><svg width="21" height="21" viewBox="0 0 21 21"><circle cx="10.5" cy="10.5" r="6" fill="none" stroke="#fff" stroke-width="1.3" stroke-dasharray="8 2"/><text x="10.5" y="13.5" text-anchor="middle" font-size="8" font-weight="700" fill="#fff" font-family="Roboto,sans-serif">$</text></svg></span>CASH FLOW<br>PROTECTION</div>
    <div class="service" style="left:189px"><span class="service-icon"><svg width="21" height="21" viewBox="0 0 21 21"><circle cx="10.5" cy="9" r="4" fill="none" stroke="#fff" stroke-width="1.3"/><path d="M5 16h11" stroke="#fff" stroke-width="1.5"/></svg></span>DEBT<br>MANAGEMENT</div>
    <div class="service dark" style="left:261px"><span class="service-icon"><svg width="21" height="21" viewBox="0 0 21 21"><path d="M4 10a6.5 6.5 0 0 1 13 0z" fill="#fff"/><path d="M10.5 10v5" stroke="#fff" stroke-width="1.2"/></svg></span>EMERGENCY<br>FUND</div>
    <div class="service" style="left:333px"><span class="service-icon"><svg width="21" height="21" viewBox="0 0 21 21"><path d="M7 7h7l-1.5 3h-4z M6 11h9v5H6z" fill="#fff"/></svg></span>BUILD WEALTH</div>
    <div class="service dark" style="left:404px"><span class="service-icon"><svg width="21" height="21" viewBox="0 0 21 21"><path d="M4 14l4-4 3 2 5-5" fill="none" stroke="#fff" stroke-width="1.3"/><rect x="11" y="12" width="6" height="4" fill="#fff"/></svg></span>PRESERVE</div>

    <div class="pill">EDUCATION &amp; AWARENESS</div>
  </section>

  <h2 class="section-heading" style="top:484px;font-size:17.5px">HOW ARE WE DOING IT?</h2>
  <div class="underline" style="left:239px;top:510px;width:36px"></div>

  <svg class="abs" style="left:44px;top:520px" width="110" height="100" viewBox="0 0 110 100">
    <path d="M20 7 A44 44 0 0 1 58 30 L44 38 A28 28 0 0 0 20 23 Z" fill="#111e33"/>
    <path d="M60 33 A44 44 0 0 1 60 67 L46 60 A28 28 0 0 0 46 40 Z" fill="#0aaf45"/>
    <path d="M58 70 A44 44 0 0 1 20 93 L20 77 A28 28 0 0 0 44 62 Z" fill="#868c95"/>
    <circle cx="20" cy="50" r="19" fill="#fff" stroke="#e3e6ea" stroke-width="2"/>
    <circle cx="20" cy="50" r="11" fill="none" stroke="#868c95" stroke-width="3"/>
    <rect x="31" y="14" width="7" height="8" rx="1" fill="#fff"/>
    <rect x="49" y="46" width="8" height="7" rx="1" fill="#fff"/>
    <rect x="31" y="78" width="7" height="6" rx="1" fill="#fff"/>
    <path d="M38 20 L48 6 H58" fill="none" stroke="#111e33" stroke-width=".6"/><circle cx="59" cy="6" r="1" fill="#111e33"/>
    <path d="M64 50 H78" fill="none" stroke="#0aaf45" stroke-width=".6"/><circle cx="79" cy="50" r="1" fill="#0aaf45"/>
    <path d="M38 82 L48 94 H58" fill="none" stroke="#868c95" stroke-width=".6"/><circle cx="59" cy="94" r="1" fill="#868c95"/>
  </svg>
  <span class="flow-label" style="left:126px;top:520px">LIVING EXPENSES</span>
  <span class="flow-label" style="left:141px;top:567px;color:var(--green)">TAXES</span>
  <span class="flow-label" style="left:126px;top:615px;color:var(--grey)">DEBT</span>

  <ul class="goal-list">
    <li><span class="tick"></span>RETIREMENT SAVINGS</li>
    <li><span class="tick"></span>CHILDREN'S EDUCATION</li>
    <li><span class="tick"></span>PROPER PROTECTION</li>
    <li><span class="tick"></span>FREEDOM FROM DEBT</li>
  </ul>

  <div class="partner" style="left:372px;top:525px"></div><div class="partner" style="left:421px;top:525px"></div>
  <div class="partner" style="left:372px;top:543px"></div><div class="partner" style="left:421px;top:543px"></div>
  <div class="partner" style="left:372px;top:562px"></div><div class="partner" style="left:421px;top:562px"></div>
  <div class="partner" style="left:372px;top:580px"></div><div class="partner" style="left:421px;top:580px"></div>
  <div class="partner" style="left:372px;top:599px"></div><div class="partner" style="left:421px;top:599px"></div>

  <footer class="footer">
    <span><svg width="6" height="6" viewBox="0 0 10 10"><path d="M2 1l2 2-1 1.5c.8 1.5 1.8 2.5 3.3 3.3L7.8 6.8l2 2L8.5 10C4 9.5.5 6 0 1.5z" fill="#fff"/></svg>+1-204-555-0148</span>|
    <span><svg width="6" height="5" viewBox="0 0 10 8"><rect width="10" height="8" fill="#fff"/><path d="M0 0l5 4 5-4" fill="none" stroke="#0aaf45"/></svg>hello@larkfieldplans.ca</span>|
    <span><svg width="6" height="6" viewBox="0 0 10 10"><circle cx="5" cy="5" r="4.3" fill="none" stroke="#fff" stroke-width="1.2"/><path d="M1 5h8M5 1v8" stroke="#fff" stroke-width=".8"/></svg>https://www.larkfieldplans.ca/</span>
  </footer>
  <div class="page-num">01</div>
</section>

<!-- PAGE TWO -->
<section class="page page-two">
  <div class="header">
    <svg width="514" height="59" viewBox="0 0 514 59">
      <rect width="514" height="59" fill="#f2f4f6"/>
      <polygon points="0,0 285,0 320,33 292,59 0,59" fill="#111e33"/>
      <polygon points="304,0 322,0 358,59 340,59" fill="#868c95"/>
      <polygon points="292,59 316,35 341,59" fill="#0aaf45"/>
    </svg>
    <h1 class="header-title">RULE OF 72</h1>
    <div class="brand"><div class="brand-name">LARKFIELD</div><div class="brand-tag">FINANCIAL PLANS</div></div>
  </div>

  <table class="rule-table">
    <colgroup><col style="width:133px"><col style="width:68px"><col style="width:84px"><col style="width:67px"><col style="width:70px"></colgroup>
    <thead><tr><th class="age">AGE</th><th>4%</th><th>6%</th><th>8%</th><th>12%</th></tr></thead>
    <tbody>
      <tr><td class="age">29</td><td>$10,000</td><td>$10,000</td><td>$10,000</td><td>$10,000</td></tr>
      <tr><td class="age">35</td><td>-</td><td>-</td><td>-</td><td>$20,000</td></tr>
      <tr><td class="age">38</td><td>-</td><td>-</td><td>$20,000</td><td>-</td></tr>
      <tr><td class="age">41</td><td>-</td><td>$20,000</td><td>-</td><td>$40,000</td></tr>
      <tr><td class="age">47</td><td>$20,000</td><td>-</td><td>$40,000</td><td>$80,000</td></tr>
      <tr><td class="age">53</td><td>-</td><td>$40,000</td><td>-</td><td>$160,000</td></tr>
      <tr><td class="age">56</td><td>-</td><td>-</td><td>$80,000</td><td>-</td></tr>
      <tr><td class="age">59</td><td>-</td><td>-</td><td>-</td><td>$320,000</td></tr>
      <tr><td class="age">65</td><td>$40,000</td><td>$80,000</td><td>$160,000</td><td>$640,000</td></tr>
    </tbody>
  </table>
  <p class="double-note" style="left:179px">MONEY DOUBLES<br>EVERY 18 YEARS</p>
  <p class="double-note" style="left:255px">MONEY DOUBLES<br>EVERY 12 YEARS</p>
  <p class="double-note" style="left:331px">MONEY DOUBLES<br>EVERY 9 YEARS</p>
  <p class="double-note" style="left:399px">MONEY DOUBLES<br>EVERY 6 YEARS</p>

  <h2 class="section-heading" style="top:389px;font-size:18px">TAXES</h2>
  <div class="underline" style="left:246px;top:412px;width:22px"></div>

  <article class="tax-card navy" style="left:46px">
    <div class="tax-icon"><svg width="31" height="31" viewBox="0 0 31 31"><path d="M7 16l8.5-7 8.5 7h-3v6h-4v-4h-3v4h-4v-6z" fill="#111e33"/></svg></div>
    <h3 class="tax-title">HOME</h3>
    <div class="tax-points"><p>Partner with mortgage brokers for best rates</p><p>Mortgage insurance alternatives</p></div>
    <div class="tax-foot">SELL</div>
  </article>
  <article class="tax-card green" style="left:154px">
    <div class="tax-icon"><svg width="31" height="31" viewBox="0 0 31 31"><rect x="9" y="9" width="13" height="13" rx="1.5" fill="#0aaf45"/><text x="15.5" y="18.5" text-anchor="middle" font-family="Roboto,sans-serif" font-size="5" font-weight="700" fill="#fff">TAX</text></svg></div>
    <h3 class="tax-title">RRSP</h3>
    <div class="tax-points"><p>Tax deduction</p><p>Tax deferred</p></div>
    <div class="tax-foot">100% TAX</div>
  </article>
  <article class="tax-card grey" style="left:262px">
    <div class="tax-icon"><svg width="31" height="31" viewBox="0 0 31 31"><rect x="9" y="17" width="3" height="5" fill="#868c95"/><rect x="13.5" y="14" width="3" height="8" fill="#868c95"/><rect x="18" y="11" width="3" height="11" fill="#868c95"/><path d="M8 15l5-4 3 2 6-5" fill="none" stroke="#868c95" stroke-width="1"/></svg></div>
    <h3 class="tax-title">TFSA</h3>
    <div class="tax-points"><p>No tax deductions</p><p>Tax free growth</p><p>2009 - $95,000</p><p>Limit 2023 - $7,000/yr</p></div>
    <div class="tax-foot">0% TAX</div>
  </article>
  <article class="tax-card navy" style="left:371px">
    <div class="tax-icon"><svg width="31" height="31" viewBox="0 0 31 31"><circle cx="17" cy="12" r="3.5" fill="none" stroke="#111e33" stroke-width="1.6"/><path d="M8 19h5l3 2h6l-6 3H8z" fill="#111e33"/></svg></div>
    <h3 class="tax-title">PERM LIFE</h3>
    <div class="tax-points"><p>No tax deduction</p><p>Qualify</p><p>Tax deferred growth</p></div>
    <div class="tax-foot">0% TAX</div>
  </article>

  <p class="cover-line">LIFE INSURANCE ILLNESS<i>/</i>CRITICAL/DISABILITY<i>/</i>DEBT MANAGEMENT<i>/</i>CASH FLOW</p>

  <footer class="footer">
    <span><svg width="6" height="6" viewBox="0 0 10 10"><path d="M2 1l2 2-1 1.5c.8 1.5 1.8 2.5 3.3 3.3L7.8 6.8l2 2L8.5 10C4 9.5.5 6 0 1.5z" fill="#fff"/></svg>+1-204-555-0148</span>|
    <span><svg width="6" height="5" viewBox="0 0 10 8"><rect width="10" height="8" fill="#fff"/><path d="M0 0l5 4 5-4" fill="none" stroke="#0aaf45"/></svg>hello@larkfieldplans.ca</span>|
    <span><svg width="6" height="6" viewBox="0 0 10 10"><circle cx="5" cy="5" r="4.3" fill="none" stroke="#fff" stroke-width="1.2"/><path d="M1 5h8M5 1v8" stroke="#fff" stroke-width=".8"/></svg>https://www.larkfieldplans.ca/</span>
  </footer>
  <div class="page-num">02</div>
</section>

</body>
</html>
```